High End Business Card Design for Flooring Store

Looking for a new card design for our hardwood flooring company. We have no print budget for these and are open to cards made from wood, metal, cardstock with embossed print ... or any combination of these. No plastic.

We sell luxury products and I want the cards to reflect our image of quality and class.

Our contact information as such;
Employee Name
418 Colbrook Blvd.
Larkvale, NS
K9R-3M5
(555) 214-3968
Employee email @velkaflooring.com

Target Market(s)

Home Builders

Contact Information for Business Card

Emnployee name, business contact information

```html
<!DOCTYPE html>
<html lang="en">
<head>
<meta charset="utf-8">
<title>Velka Flooring – Business Card</title>
<link href="https://fonts.googleapis.com/css2?family=Montserrat:wght@400;500;600;700&display=swap" rel="stylesheet">
<style>
  :root {
    --gold: #e5b32a;
    --red: #962b22;
    --ink: #1f1f1f;
    --card-black: #1d1d1e;
    --emboss: #2e2e30;
    --paper: #ffffff;
    --backdrop: #d9d9d6;
  }
  * { box-sizing: border-box; margin: 0; padding: 0; }
  html, body { width: 1200px; height: 913px; overflow: hidden; }
  body {
    background: var(--backdrop);
    font-family: "Montserrat", Arial, sans-serif;
    position: relative;
  }
  .card {
    position: absolute;
    width: 540px;
    height: 308px;
    border-radius: 16px;
    overflow: hidden;
  }
  .card--front {
    left: 70px; top: 120px;
    background: var(--card-black);
    border: 3px solid var(--gold);
  }
  .front-brand {
    position: absolute;
    left: 0; right: 0; top: 110px;
    text-align: center;
    font-size: 76px;
    font-weight: 600;
    color: var(--emboss);
    letter-spacing: 1px;
  }
  .card--back {
    left: 590px; top: 470px;
    background: var(--paper);
    border: 2px solid var(--gold);
  }
  .back-band { position: absolute; inset: 0; }
  .brand {
    position: absolute;
    left: 42px; top: 128px;
    display: flex; align-items: center; gap: 10px;
  }
  .brand-square { width: 26px; height: 26px; background: var(--gold); }
  .brand-name {
    font-size: 48px; font-weight: 600; color: var(--red); line-height: 1;
  }
  .divider {
    position: absolute;
    left: 262px; top: 60px;
    width: 1px; height: 160px;
    background: var(--gold);
  }
  .contact {
    position: absolute;
    left: 284px; top: 38px;
    color: var(--ink);
    font-size: 12.5px;
    line-height: 18px;
  }
  .person-name { font-size: 25px; font-weight: 700; line-height: 30px; }
  .person-name .first { color: var(--gold); }
  .person-name .last { color: var(--red); }
  .role { margin-bottom: 6px; }
  .address { margin-bottom: 8px; }
  .contact-row { display: flex; align-items: center; gap: 7px; line-height: 20px; }
  .contact-row svg { width: 12px; height: 12px; flex: none; }
</style>
</head>
<body>

<section class="card card--front" aria-label="Card front">
  <div class="front-brand">Velka</div>
</section>

<section class="card card--back" aria-label="Card back">
  <svg class="back-band" viewBox="0 0 540 308" preserveAspectRatio="none" aria-hidden="true">
    <path d="M0 308 L0 298 L360 250 C390 246 396 224 420 220 L540 202 L540 308 Z" fill="var(--red)"/>
    <path d="M0 289 L352 241" stroke="var(--gold)" stroke-width="5" fill="none"/>
  </svg>

  <div class="brand">
    <span class="brand-square"></span>
    <span class="brand-name">Velka</span>
  </div>

  <div class="divider"></div>

  <div class="contact">
    <p class="person-name"><span class="first">Employee</span> <span class="last">Name</span></p>
    <p class="role">Owner/CEO</p>
    <p class="address">418 Colbrook Blvd.<br>Larkvale, NS<br>K9R-3M5</p>
    <p class="contact-row">
      <svg viewBox="0 0 12 12"><path d="M2 1 L4.5 1 L5.5 3.5 L4 4.6 C4.7 6 6 7.3 7.4 8 L8.5 6.5 L11 7.5 L11 10 C11 10.6 10.6 11 10 11 C5 11 1 7 1 2 C1 1.4 1.4 1 2 1 Z" fill="var(--gold)"/></svg>
      (555) 214-3968
    </p>
    <p class="contact-row">
      <svg viewBox="0 0 12 12"><rect x="0.5" y="2" width="11" height="8" rx="1" fill="var(--gold)"/><path d="M1 2.5 L6 6.5 L11 2.5" stroke="#fff" stroke-width="1" fill="none"/></svg>
      info@velkaflooring.com
    </p>
    <p class="contact-row">
      <svg viewBox="0 0 12 12"><circle cx="6" cy="6" r="5.5" fill="var(--gold)"/><path d="M0.5 6 H11.5 M6 0.5 C3.5 3 3.5 9 6 11.5 M6 0.5 C8.5 3 8.5 9 6 11.5" stroke="#fff" stroke-width="0.8" fill="none"/></svg>
      www.velkaflooring.com
    </p>
  </div>
</section>

</body>
</html>
```